Business Card Design for Kidvale (Hires out childrens play areas)

Looking to have a business card designed for a company we just bought. The company rents out childrens play areas.

I have uploaded a couple of examples of the kind of business card style I like. Here are two more examples:

https://quorvastudio.nz/project/bright-romp-branding/
https://imgvaultcdn.com/design_img/8841052/302917/302917_5518203_8841052_b73e19a2_image.jpg

I think a white card will be best due to all the colours in the logo.

Size we require: 3.75" x 2.25" (horizontally orientated) with a 0.125" bleed

Uploaded is two versions of our logo.

Details for the card:
1. My name: Liam Verster
2. Title: Managing Director
3. Phone no: 021 563 417
4. Email: liam@kidvale.co.nz
5. URL: www.kidvale.co.nz
6. Address:
PO Box 318625
Fernlea, Auckland

Let me know if you need anything else.

Target Market(s)

Hospitals, doctors surgeries, bed shops, etc.

Contact Information for Business Card

Details for the card:
1. My name: Liam Verster
3. Phone no: 021 563 417
5. URL: www.kidvale.co.nz
6. Address:
PO Box 318625
Fernlea, Auckland

Requirements
Should not have
• Not too busy.

```html
<!DOCTYPE html>
<html lang="en">
<head>
<meta charset="utf-8">
<title>Kidvale Business Card</title>
<link rel="stylesheet" href="https://fonts.googleapis.com/css2?family=Roboto:wght@400;500;700&display=swap">
<style>
  :root {
    --backdrop: #3b322e;
    --card-dark: #2c2c2e;
    --card-edge: #1d4c9e;
    --card-light: #fbfbfb;
    --brand-blue: #1f56b3;
    --ink: #4a4a4a;
    --rule: #d2d2d2;
    --teal: #1aa3ac;
    --red: #e0202e;
    --green: #3bab47;
    --orange: #f39a1e;
  }
  * { box-sizing: border-box; margin: 0; padding: 0; }
  html, body { width: 1200px; height: 856px; overflow: hidden; }
  body {
    background: var(--backdrop);
    font-family: "Roboto", Arial, sans-serif;
    position: relative;
  }
  .card {
    position: absolute;
    width: 560px;
    height: 336px;
    border-radius: 3px;
    box-shadow: 0 10px 28px rgba(0,0,0,.45);
    overflow: hidden;
  }
  .card-front {
    left: 70px; top: 70px;
    background: var(--card-dark);
    border-bottom: 6px solid var(--card-edge);
    display: flex; align-items: center; justify-content: center;
  }
  .card-back {
    left: 570px; top: 450px;
    background: var(--card-light);
  }
  .wordmark {
    display: flex; align-items: center; gap: 14px;
    font-weight: 700;
    color: var(--brand-blue);
    letter-spacing: .5px;
  }
  .wordmark-dot {
    border-radius: 50%;
    background: var(--orange);
    flex: none;
  }
  .card-front .wordmark { font-size: 64px; color: #ffffff; }
  .card-front .wordmark-dot { width: 44px; height: 44px; }
  .card-back .wordmark {
    position: absolute; left: 40px; top: 112px;
    font-size: 38px;
  }
  .card-back .wordmark-dot { width: 28px; height: 28px; }
  .divider {
    position: absolute; left: 268px; top: 70px;
    width: 1px; height: 170px;
    background: var(--rule);
  }
  .details {
    position: absolute; left: 292px; top: 72px;
    color: var(--ink);
    font-size: 14px; line-height: 1.45;
  }
  .person-name { color: var(--brand-blue); font-weight: 700; font-size: 22px; line-height: 1.1; }
  .person-title { font-size: 14px; margin-bottom: 12px; }
  .address { margin-bottom: 10px; }
  .contact-line { display: flex; align-items: center; gap: 8px; }
  .contact-line svg { width: 13px; height: 13px; flex: none; }
  .colour-band {
    position: absolute; left: 0; right: 0; bottom: 0;
    height: 12px; display: flex; gap: 5px;
  }
  .colour-band span { flex: 1; }
  .band-teal { background: var(--teal); }
  .band-red { background: var(--red); }
  .band-green { background: var(--green); }
  .band-orange { background: var(--orange); }
</style>
</head>
<body>
  <section class="card card-front">
    <div class="wordmark"><span class="wordmark-dot"></span>Kidvale</div>
  </section>

  <section class="card card-back">
    <div class="wordmark"><span class="wordmark-dot"></span>Kidvale</div>
    <div class="divider"></div>
    <div class="details">
      <div class="person-name">Liam Verster</div>
      <div class="person-title">Managing Director</div>
      <div class="address">PO Box 318625<br>Fernlea, Auckland</div>
      <div class="contact-line">
        <svg viewBox="0 0 16 16" aria-hidden="true"><path d="M4 1.5l2.2 3-1.3 1.6c.9 2 2.5 3.6 4.5 4.5l1.6-1.3 3 2.2-1.3 2.5C7.5 14 2 8.5 1.5 3z" fill="var(--teal)"/></svg>
        <span>021 563 417</span>
      </div>
      <div class="contact-line">
        <svg viewBox="0 0 16 16" aria-hidden="true"><rect x="1.5" y="3.5" width="13" height="9" fill="none" stroke="var(--green)" stroke-width="1.4"/><path d="M1.5 3.5L8 9l6.5-5.5" fill="none" stroke="var(--green)" stroke-width="1.4"/></svg>
        <span>liam@kidvale.co.nz</span>
      </div>
      <div class="contact-line">
        <svg viewBox="0 0 16 16" aria-hidden="true"><circle cx="8" cy="8" r="6.3" fill="none" stroke="var(--orange)" stroke-width="1.4"/><ellipse cx="8" cy="8" rx="2.8" ry="6.3" fill="none" stroke="var(--orange)" stroke-width="1.2"/><path d="M1.7 8h12.6" stroke="var(--orange)" stroke-width="1.2"/></svg>
        <span>www.kidvale.co.nz</span>
      </div>
    </div>
    <div class="colour-band">
      <span class="band-teal"></span><span class="band-red"></span><span class="band-green"></span><span class="band-orange"></span>
    </div>
  </section>
</body>
</html>
```